Cosmetic injections clinic needs a fresh looking business card

We need a business card using the supplied logo and color scheme to attract future clients to our clinic. It should be modern and fresh, eye catching and not too busy. Simple and to the point is best. I would like two sided designs with the front indicating address and contact information, and the back in full color with white logo and descriptive information also provided.
Target Market(s)
Clients looking for non surgical beauty enhancements.
Contact Information for Business Card
MeloraSkin
14, 618 Birchmont Way
St. Albert, Alberta
K2P 7W3
Phone: 587-412-6630
Email: info@meloraskin.com
Requirements
Must have
- -Logo supplied with the name and address of the clinic
- -Back of card in full color with white logo with A small line of text indicating both of the following: Anti aging consultants and cosmetic injectables
- Located inside the Voyager Wellness Group

```html
<!DOCTYPE html>
<html lang="en">
<head>
<meta charset="utf-8">
<title>MeloraSkin Business Card</title>
<link href="https://fonts.googleapis.com/css2?family=Arimo:wght@400;700&display=swap" rel="stylesheet">
<style>
  :root {
    --stage: #2b2b2d;
    --card-white: #ffffff;
    --purple: #6a3d9e;
    --purple-deep: #56308a;
    --purple-light: #7a4cb0;
    --pink: #d9378f;
    --pink-line: #e889bd;
    --ink-grey: #555555;
  }
  * { margin: 0; padding: 0; box-sizing: border-box; }
  html, body {
    width: 1200px; height: 997px; overflow: hidden;
    background: var(--stage);
    font-family: "Arimo", Arial, sans-serif;
  }
  .stage { position: relative; width: 1200px; height: 997px; }

  .card {
    position: absolute;
    width: 520px; height: 297px;
    border-radius: 4px;
    overflow: hidden;
    box-shadow: 0 18px 40px rgba(0,0,0,.45);
  }

  /* Front */
  .card-front { left: 70px; top: 150px; background: var(--card-white); }
  .card-front .bands { position: absolute; inset: 0; }
  .brand-lockup {
    position: absolute; left: 44px; top: 52px;
    display: flex; align-items: center; gap: 12px;
  }
  .brand-dot { width: 34px; height: 34px; border-radius: 50%; background: var(--purple); }
  .brand-name { font-weight: 700; font-size: 34px; color: var(--purple); letter-spacing: .5px; }
  .divider {
    position: absolute; left: 170px; right: 30px; top: 140px;
    height: 1px; background: var(--pink-line);
  }
  .person { position: absolute; left: 30px; top: 162px; }
  .person-name { font-size: 17px; color: var(--purple); }
  .person-role { font-size: 12px; color: var(--pink); margin-top: 2px; }
  .contact-list { position: absolute; left: 30px; top: 208px; list-style: none; }
  .contact-list li {
    display: flex; align-items: center; gap: 8px;
    font-size: 12px; color: var(--ink-grey); margin-bottom: 6px;
  }
  .contact-icon {
    width: 14px; height: 14px; border-radius: 50%;
    background: var(--pink); display: flex; align-items: center; justify-content: center;
  }
  .address { position: absolute; right: 30px; top: 70px; text-align: right; }
  .address-name { font-size: 16px; color: var(--pink); letter-spacing: .5px; }
  .address-line { font-size: 11px; color: var(--ink-grey); margin-top: 3px; }
  .website {
    position: absolute; right: 26px; bottom: 13px;
    font-size: 14px; color: var(--card-white); letter-spacing: .5px;
  }

  /* Back */
  .card-back {
    left: 610px; top: 430px;
    background: linear-gradient(135deg, var(--purple-light), var(--purple) 55%, var(--purple-deep));
  }
  .card-back .brand-lockup { left: 50%; top: 50%; transform: translate(-50%, -58%); gap: 16px; }
  .card-back .brand-dot { width: 54px; height: 54px; background: var(--card-white); }
  .card-back .brand-name { font-size: 52px; color: var(--card-white); }
  .tagline {
    position: absolute; left: 26px; right: 20px; bottom: 22px;
    font-size: 11px; color: var(--card-white); opacity: .9;
  }
</style>
</head>
<body>
<main class="stage">

  <section class="card card-front" aria-label="Business card front">
    <svg class="bands" viewBox="0 0 520 297" aria-hidden="true">
      <path d="M0 270 H315 C333 270 333 240 357 240 H520 V245 H360 C338 245 338 276 318 276 H0 Z" fill="var(--purple)"/>
      <path d="M0 282 H320 C340 282 340 250 362 250 H520 V297 H0 Z" fill="var(--pink)"/>
    </svg>
    <div class="brand-lockup">
      <span class="brand-dot"></span>
      <span class="brand-name">MeloraSkin</span>
    </div>
    <div class="divider"></div>
    <div class="address">
      <p class="address-name">MELORASKIN</p>
      <p class="address-line">14, 618 Birchmont Way</p>
      <p class="address-line">St. Albert, Alberta K2P 7W3</p>
    </div>
    <div class="person">
      <p class="person-name">Dana Whitfield</p>
      <p class="person-role">Director</p>
    </div>
    <ul class="contact-list">
      <li>
        <span class="contact-icon">
          <svg width="8" height="8" viewBox="0 0 10 10" aria-hidden="true"><path d="M2 1 L4 1 L5 3 L4 4 C4.5 5.5 5 6 6 6.5 L7 5.5 L9 6.5 L9 8.5 C5 9 1 5 2 1 Z" fill="#fff"/></svg>
        </span>
        587-412-6630
      </li>
      <li>
        <span class="contact-icon">
          <svg width="8" height="8" viewBox="0 0 10 10" aria-hidden="true"><rect x="1" y="2.5" width="8" height="5.5" fill="none" stroke="#fff" stroke-width="1.2"/><path d="M1 2.5 L5 6 L9 2.5" fill="none" stroke="#fff" stroke-width="1.2"/></svg>
        </span>
        info@meloraskin.com
      </li>
    </ul>
    <p class="website">www.meloraskin.com</p>
  </section>

  <section class="card card-back" aria-label="Business card back">
    <div class="brand-lockup">
      <span class="brand-dot"></span>
      <span class="brand-name">MeloraSkin</span>
    </div>
    <p class="tagline">Anti aging consultants and cosmetic injectables. Located inside the Voyager Wellness Group</p>
  </section>

</main>
</body>
</html>
```